Packaging design for high end, natural skin care line needed

Marisol Thackery Beauty needs a label design. It is a new skin care line I am launching.
For years my line Velvet Orchard Beauty was quite popular and featured in several magazines, but for personal reasons had to be shut down. Now I am launching a new line featuring VOB's top selling products, but focused solely on skin care more so than cosmetics. All products will still be handmade, but the line should still look professional-something worthy of a Brindle Market shelf!
I am branding it with my name, as I am often quoted in articles related to gluten in beauty products, so Marisol Thackery and beauty are key words.
The key products will be facial and body serums which are packaged in .5oz., 1oz. and larger amber glass bottles with black dropper tops, I will include pictures below. For dimensions, the labels can be any size that you think will work best, but need to at the least fit the 1oz. bottle, dimensions shown here http://www.corvelflask.example/amber-glass-tall-round-flask/p/QZ7K-93/
I loved the former VOB logo, but for Marisol Thackery Beauty I am looking for something more personal, more apothecary-like, and probably less colorful.
The line will be small, just a handful of products, but luxe, rich.
I am attaching photos of Velvet Orchard Beauty's packaging for your reference.
Thanks much!!

Hi Everyone! Thank you for your submissions! Please see the links I provided in the brief, I really am looking for something more technical looking, like an apothecary. And want black text on a white background, not a black background, and nothing flowery.
Thank you all!!
Marisol

Target Market(s)

My clients are primarily women of all ages, but with more of a skin care focus, and no longer a cosmetic one, I would also like to appeal to a male audience. My clients are health conscious, gluten-free, natural, paleo, or vegan, etc. Target age is probably 25-55. Products are a bit high end, priced $45-65.

Industry/Entity Type

Cosmetics

Requirements
Must have
• It must at least say Marisol Thackery, or can say Marisol Thackery Beauty, but "Beauty" is not necessary. And capitalization is open, try whatever you think serves the brand. Likely slogans or taglines that can be included but are not essential: Care for your skin. Love and care for your skin. Handmade with love in the USA. Handmade in the USA. Think modern day apothecary. Small batch scotch. Something fine, but custom, handmade.
Nice to have
• I like the aesthetic of Oribel Skin Care a bit http://www.oribelhollis.example.au/
And of Dorian Valtz as shown here http://www.pinboardia.example/pin/847302915563017442/
Also of something like this that is even customizable http://www.pinboardia.example/pin/58274106392285514/
Every product is handmade in small batches, with fine ingredients, a moderate price point of around $45-$65. And I will likely begin making custom orders. So there could be a space to say when it was made, or for whom. I would like to keep the colors classic though, I probably want to stay away from the bright pink on this one.
Should not have
• As I mentioned, probably want to stay away from a lot of color. I like black vs. gray for the text, as it will show up better in editorials. I must look good, but also photograph well. Thanks!

```html
<!DOCTYPE html>
<html lang="en">
<head>
<meta charset="utf-8">
<title>Marisol Thackery Beauty – Serum Label</title>
<link href="https://fonts.googleapis.com/css2?family=Roboto+Condensed:wght@700&family=Inter:wght@500;700&family=Courier+Prime&family=Mr+Dafoe&display=swap" rel="stylesheet">
<style>
  :root {
    --backdrop: #eeeeee;
    --label: #ffffff;
    --ink: #262626;
    --ink-soft: #4a4a4a;
    --ink-muted: #6b6b6b;
    --rule: #8a8a8a;
    --signature: #e3202b;
  }
  * { margin: 0; padding: 0; box-sizing: border-box; }
  html, body {
    width: 1200px;
    height: 1000px;
    overflow: hidden;
    background: var(--backdrop);
  }
  .canvas {
    position: relative;
    width: 1200px;
    height: 1000px;
  }
  .label {
    position: absolute;
    left: 294px;
    top: 100px;
    width: 612px;
    height: 800px;
    background: var(--label);
    border-bottom-right-radius: 190px;
    box-shadow: 0 2px 10px rgba(0,0,0,0.06);
  }
  .tagline {
    position: absolute;
    left: 42px;
    top: 50px;
    font-family: "Inter", sans-serif;
    font-weight: 700;
    font-size: 15px;
    letter-spacing: 0.34em;
    color: var(--ink);
    white-space: nowrap;
  }
  .brand-name {
    position: absolute;
    left: 38px;
    top: 100px;
    font-family: "Roboto Condensed", sans-serif;
    font-weight: 700;
    font-size: 112px;
    line-height: 0.92;
    letter-spacing: -0.02em;
    color: var(--ink);
    text-transform: uppercase;
    white-space: nowrap;
  }
  .brand-descriptor {
    position: absolute;
    left: 42px;
    top: 316px;
    font-family: "Courier Prime", monospace;
    font-size: 48px;
    line-height: 1;
    color: var(--ink-soft);
  }
  .made-for {
    position: absolute;
    left: 42px;
    top: 400px;
    width: 530px;
    height: 64px;
    border-bottom: 2px solid var(--rule);
  }
  .made-for__label {
    position: absolute;
    left: 4px;
    bottom: 8px;
    font-family: "Inter", sans-serif;
    font-weight: 500;
    font-size: 10px;
    letter-spacing: 0.18em;
    color: var(--ink-muted);
  }
  .made-for__name {
    position: absolute;
    left: 138px;
    bottom: -6px;
    font-family: "Mr Dafoe", cursive;
    font-size: 54px;
    line-height: 1;
    color: var(--signature);
    white-space: nowrap;
  }
  .house-mark {
    position: absolute;
    left: 42px;
    top: 540px;
    display: flex;
    align-items: center;
    gap: 14px;
  }
  .house-mark__square {
    width: 16px;
    height: 16px;
    background: var(--ink-soft);
  }
  .house-mark__name {
    font-family: "Inter", sans-serif;
    font-weight: 700;
    font-size: 18px;
    letter-spacing: 0.24em;
    color: var(--ink-soft);
    text-transform: uppercase;
    white-space: nowrap;
  }
  .product-notes {
    position: absolute;
    left: 42px;
    top: 664px;
    font-family: "Courier Prime", monospace;
    font-size: 24px;
    line-height: 29px;
    color: var(--ink-muted);
    text-transform: uppercase;
  }
  .product-notes .volume { text-transform: none; }
</style>
</head>
<body>
  <main class="canvas">
    <section class="label" aria-label="Serum bottle label">
      <p class="tagline">LOVE AND CARE FOR YOUR SKIN</p>
      <h1 class="brand-name">Marisol<br>Thackery</h1>
      <p class="brand-descriptor">BEAUTY</p>
      <div class="made-for">
        <span class="made-for__label">MADE FOR</span>
        <span class="made-for__name">Lena Whitcombe</span>
      </div>
      <div class="house-mark">
        <span class="house-mark__square"></span>
        <span class="house-mark__name">Velvet Orchard Beauty</span>
      </div>
      <p class="product-notes">
        Natural gluten free<br>
        Cosmetics &amp; skin care<br>
        <span class="volume">1fl oz</span>
      </p>
    </section>
  </main>
</body>
</html>
```